Kravin House Music DJ Chatterly Banner

Hi there,
This is for a house music dj Chatterly site. Looking for the top banner to replace my page. You can check put Kravin on Chatterly to see the banner.
The name Kravin is pronounced like Fossil. use Dinosaurs a lot in my music. The whole idea is because I an older DJ. A fossil. I need a cool banner I can also use on Chatterly and Blinkpost.

https://www.chatterlyhub.com/Kravin

Target Market(s)

Target market is people who enjoy house music, EDM, dance music, etc.

Industry/Entity Type

House

Font styles to use
Sans Serif

Requirements
Must have
• The banner must be modern and cool looking appealing to EDM music lovers
• Must be reflective of my "fossil" theme but use my dj name Kravin
Nice to have
• Dinosaur feel but not cartoony.
• Steel or fossil look
Should not have
• DO NOT say DJ KRAVIN. Only Kravin
• Do not use the uploads in the design. Looking for a new concept completely

```html
<!DOCTYPE html>
<html lang="en">
<head>
<meta charset="utf-8">
<title>Kravin Banner</title>
<link rel="stylesheet" href="https://fonts.googleapis.com/css2?family=Bebas+Neue&display=swap">
<style>
  :root {
    --bg-dark: #160f13;
    --bg-maroon: #34191f;
    --bone: #a8825c;
    --bone-light: #c29c74;
    --moss: #4c6446;
    --rust: #a0604e;
    --white: #ffffff;
  }
  html, body {
    margin: 0;
    padding: 0;
    width: 1200px;
    height: 450px;
    overflow: hidden;
    background: var(--bg-dark);
  }
  .banner {
    position: relative;
    width: 1200px;
    height: 450px;
    overflow: hidden;
    background: linear-gradient(115deg, var(--bg-dark) 0%, #1f1418 45%, var(--bg-maroon) 75%, #1c1216 100%);
  }
  .fossil-photo {
    position: absolute;
    left: 0;
    top: 0;
    width: 960px;
    height: 450px;
    background: linear-gradient(100deg,
      var(--bone) 0%,
      var(--bone-light) 14%,
      #8c6c50 26%,
      var(--moss) 42%,
      #6a6048 52%,
      var(--rust) 64%,
      var(--moss) 78%,
      rgba(52,25,31,0) 100%);
    -webkit-mask-image: radial-gradient(ellipse 78% 95% at 45% 55%, #000 55%, transparent 100%);
    mask-image: radial-gradient(ellipse 78% 95% at 45% 55%, #000 55%, transparent 100%);
    opacity: 0.85;
  }
  .stripes {
    position: absolute;
    inset: 0;
    background: repeating-linear-gradient(-25deg, rgba(255,255,255,0.06) 0 24px, transparent 24px 52px);
  }
  .title-block {
    position: absolute;
    left: 312px;
    top: 127px;
    width: 577px;
    height: 197px;
  }
  .rule {
    position: absolute;
    left: 0;
    width: 100%;
    height: 5px;
    background: var(--white);
  }
  .rule.top { top: 0; }
  .rule.bottom { bottom: 0; }
  .title {
    position: absolute;
    inset: 0;
    margin: 0;
    display: flex;
    align-items: center;
    justify-content: center;
    font-family: "Bebas Neue", "Oswald", sans-serif;
    font-weight: 400;
    font-size: 230px;
    line-height: 1;
    letter-spacing: 12px;
    padding-top: 16px;
    padding-left: 12px;
    color: var(--white);
  }
</style>
</head>
<body>
  <div class="banner">
    <div class="fossil-photo" role="img" aria-label="Photograph of a dinosaur fossil skeleton: skull with open jaws and teeth at centre, spine and ribs on the left, toned in bone, moss green and rust"></div>
    <div class="stripes"></div>
    <div class="title-block">
      <div class="rule top"></div>
      <h1 class="title">KRAVIN</h1>
      <div class="rule bottom"></div>
    </div>
  </div>
</body>
</html>
```